Business card and stationary design for a digital advertising agency

We look to get designs for
- Business card
- Envelope C5 & A4
- Letterhead A4
- Thin Folder (to place the brochures and quotes in. There must be places to put the cd envelope and a business card inside the file as well as a place for the papers)
- CD label & envelope
- Notepad
- Mousepad

We are open for all kind of creativity but please have a look at our website to have an idea. (The website is not ready at the moment but you can see the colours, get the logo, etc.)

Link: www.trelvanix.com/anasayfa

PLEASE NOTE: In the logo file, there are 2 logos but we only use the one on top. We never use the one at the bottom!
Updates

Please use the attached ForDesign.zip file to use the background pattern of our website, inside the folder img there are background patterns of our website. Please use the background or at least inspire from that files in order to design our brochures.  

All designers, please bear in mind that firstly we need the samples of each items described in the brief. Then we will comment on each of them. 

Please submit the designs for all the items at once.

Thanks!

TrelVanix

Target Market(s)

Our customers are the companies who will advertise on internet and digital media and we work mainly in Turkish market

Industry/Entity Type

Digital

Requirements
Must have
• Please use the attached ForDesign.zip file to use the background pattern of our website, inside the folder img there are background patterns of our website. Please use the background or at least inspire from that files in order to design our brochures.
Should not have
• Too much colours such as a child's colouring book.

```html
<!DOCTYPE html>
<html lang="en">
<head>
<meta charset="utf-8">
<title>TrelVanix Mouse Pad</title>
<link rel="stylesheet" href="https://fonts.googleapis.com/css2?family=Mulish:wght@700;800&display=swap">
<style>
  :root {
    --page-bg: #efece7;
    --pad-green: #b7d37a;
    --pad-lime: #d9e36a;
    --pad-yellow: #f4dc5a;
    --pad-orange: #f19a3e;
    --pad-pink: #e47aa8;
    --pad-blue: #8fb8d6;
    --pad-shade: #4e5150;
    --label-bg: #ffffff;
    --brand-ink: #4a4a4a;
    --brand-dot: #d9327a;
    --contact-ink: #1e1e1e;
  }
  * { margin: 0; padding: 0; box-sizing: border-box; }
  html, body { width: 1200px; height: 849px; overflow: hidden; }
  body {
    background: var(--page-bg);
    font-family: "Mulish", Arial, sans-serif;
    position: relative;
  }
  .mouse-pad {
    position: absolute;
    left: 230px;
    top: 114px;
    width: 740px;
    height: 620px;
    border-radius: 38px;
    overflow: hidden;
    box-shadow: 0 4px 14px rgba(0,0,0,0.18);
  }
  .pad-artwork {
    position: absolute;
    inset: 0;
    background:
      radial-gradient(circle at 40% 12%, rgba(241,120,62,0.55), transparent 18%),
      radial-gradient(circle at 88% 38%, rgba(238,80,60,0.55), transparent 16%),
      radial-gradient(circle at 58% 72%, rgba(228,122,168,0.6), transparent 20%),
      radial-gradient(circle at 75% 52%, rgba(241,154,62,0.6), transparent 18%),
      radial-gradient(circle at 82% 12%, rgba(244,220,90,0.7), transparent 22%),
      radial-gradient(circle at 8% 45%, rgba(143,184,214,0.7), transparent 26%),
      radial-gradient(circle at 30% 60%, rgba(170,150,210,0.5), transparent 22%),
      linear-gradient(180deg, transparent 78%, var(--pad-shade) 100%),
      linear-gradient(135deg, var(--pad-blue) 0%, var(--pad-green) 40%, var(--pad-lime) 75%, var(--pad-green) 100%);
  }
  .contact-label {
    position: absolute;
    left: 0;
    top: 397px;
    width: 223px;
    height: 147px;
    background: var(--label-bg);
    border-radius: 0 12px 12px 0;
    padding: 20px 0 0 44px;
  }
  .brand-name {
    display: flex;
    align-items: center;
    gap: 6px;
    font-weight: 800;
    font-size: 25px;
    letter-spacing: -0.5px;
    color: var(--brand-ink);
    margin-left: -2px;
  }
  .brand-dot {
    width: 8px;
    height: 8px;
    border-radius: 50%;
    background: var(--brand-dot);
  }
  .contact-list {
    list-style: none;
    margin-top: 30px;
    font-weight: 700;
    font-size: 8.2px;
    line-height: 12.5px;
    color: var(--contact-ink);
  }
  .contact-key { margin-right: 2px; }
</style>
</head>
<body>
  <main class="mouse-pad">
    <div class="pad-artwork" role="img" aria-label="Background pattern of overlapping translucent rounded squares in green, yellow, orange, pink and blue"></div>
    <section class="contact-label">
      <div class="brand-name"><span>TrelVanix</span><span class="brand-dot"></span></div>
      <ul class="contact-list">
        <li><span class="contact-key">C:</span> 0735 412 906 / 0721 638 204</li>
        <li><span class="contact-key">W:</span> www.trelvanix.com/anasayfa</li>
        <li><span class="contact-key">E:</span> kmorel@trelvanix.com</li>
        <li><span class="contact-key">M:</span> P.o Box 318704 Earth.</li>
      </ul>
    </section>
  </main>
</body>
</html>
```